Professional consulting firm needing a Word document template

I need a Word document template that can be used flexibly for a flyer or brochure of 1 to 3 pages in length. The first page should be designed in a way that it can stand alone as a one-page flyer without a formal cover page. I have attached sample text as a Word document that could be used as the basis for the first 1-2 pages, however I do need three page layouts designed to give flexibility to use as a 3 page booklet. I have attached our brand guidelines, logo, and some stock images that I have previously purchased (they may not all be useful but it gives some options). <br/>The Word document needs to be set up in away that it can easily be edited to accommodate updates to the text, and some variation in the quantity of text on each page. Each page should be able to accommodate a mixture of paragraph text, bullet points, small boxes to call out highlights, one or more images, and some white space to avoid clutter. It should look professional yet engaging and modern.

Font styles to use
Sans Serif

Requirements
Must have
• Must be an editable Microsoft Word document, using the text provided. Must be a layout suitable to use as 1 page, up to 3 pages. Must comply with brand guidelines.

```html
<!DOCTYPE html>
<html lang="en">
<head>
<meta charset="utf-8">
<title>MS Word Template Design</title>
<link href="https://fonts.googleapis.com/css2?family=Hind:wght@300;400;500;600;700&display=swap" rel="stylesheet">
<style>
  :root {
    --board: #58f8fb;
    --board-light: #8ffbfd;
    --paper: #ffffff;
    --cyan: #35d9ea;
    --purple: #8a1be0;
    --navy: #1b2340;
    --ink: #2a2f3a;
    --rule: #3a3f4a;
    --pattern: #d6f3f8;
  }
  * { box-sizing: border-box; margin: 0; padding: 0; }
  html, body { width: 1200px; height: 849px; overflow: hidden; }
  body {
    position: relative;
    background: var(--board);
    font-family: "Hind", Arial, sans-serif;
    color: var(--ink);
  }
  .board-pattern {
    position: absolute; left: 949px; top: 0; width: 251px; height: 267px;
    background: radial-gradient(ellipse at 75% 30%, var(--board-light) 0%, rgba(143,251,253,0.55) 45%, rgba(88,248,251,0) 75%);
  }
  .board-title {
    position: absolute; left: 52px; top: 112px;
    color: var(--paper); font-weight: 700; font-size: 42px; line-height: 44px;
    letter-spacing: -0.5px;
  }
  .page {
    position: absolute; top: 316px; width: 266px; height: 376px;
    background: var(--paper);
    box-shadow: 0 6px 18px rgba(0, 90, 110, 0.25);
    overflow: hidden;
  }
  .page--1 { left: 52px; }
  .page--2 { left: 329px; }
  .page--3 { left: 605px; }
  .page--4 { left: 882px; }
  .abs { position: absolute; }
  .photo { position: absolute; }
  .corner-pattern {
    position: absolute; right: 0; top: 0; width: 80px; height: 81px;
    background: radial-gradient(ellipse at 85% 20%, var(--pattern) 0%, rgba(214,243,248,0.7) 45%, rgba(255,255,255,0) 72%);
  }
  .tab { position: absolute; left: 22px; top: 25px; width: 25px; height: 12px; background: var(--purple); }
  .heading {
    position: absolute; color: var(--cyan); font-size: 9.5px; line-height: 11.5px; text-transform: uppercase;
  }
  .heading .light { font-weight: 300; }
  .heading .bold { font-weight: 700; }
  .copy { font-size: 4.4px; line-height: 6.4px; color: var(--ink); }
  .copy p + p { margin-top: 4px; }
  .bullets { list-style: none; margin-top: 4px; }
  .bullets li { position: relative; padding-left: 16px; }
  .bullets li::before { content: "•"; position: absolute; left: 1px; }
  .item-label { color: var(--cyan); }
  .rule { position: absolute; height: 0.6px; background: var(--cyan); }
  .callout-title { color: var(--cyan); font-weight: 700; }
  .callout-body { font-style: italic; }
  .brand {
    position: absolute; font-weight: 700; font-size: 13px; letter-spacing: 0.6px; color: var(--navy);
  }
  .footer-rule { position: absolute; left: 22px; top: 356px; width: 224px; height: 0.6px; background: var(--rule); }
  .footer {
    position: absolute; left: 20px; top: 362px; width: 228px;
    display: flex; justify-content: space-between;
    font-size: 4.2px; color: var(--cyan);
  }
  .quote-bar { position: absolute; left: 21px; top: 297px; width: 4px; height: 39px; background: var(--purple); }
  .quote { position: absolute; left: 30px; top: 302px; width: 110px; font-size: 6.6px; line-height: 8.6px; font-weight: 600; color: var(--cyan); }
</style>
</head>
<body>
  <div class="board-pattern" role="img" aria-label="Soft decorative brand pattern of rounded shapes"></div>
  <h1 class="board-title">MS WORD<br>TEMPLATE DESIGN</h1>

  <!-- Page 1 -->
  <section class="page page--1">
    <div class="photo" style="left:0;top:0;width:266px;height:128px;background:linear-gradient(180deg,#3a3f8a 0%,#7a5fa8 35%,#e98a8a 55%,#5a4a3a 80%,#2a2620 100%);" role="img" aria-label="Photo of a train speeding past railway tracks at sunset"></div>
    <h2 class="heading" style="left:20px;top:166px;width:200px;">
      <span class="light">Train Driver Competency</span><br>
      <span class="bold">Indicator Development<br>Project.</span>
    </h2>
    <div class="copy abs" style="left:22px;top:212px;width:110px;">
      <p>We are commencing an applied research project to develop and test a framework of underlying core competencies for train driver performance. The objective of the project is to identify observable indicators that describe effective performance in the following types of underlying competencies:</p>
      <ul class="bullets">
        <li>Application of Procedures</li>
        <li>Communication</li>
        <li>Operation of Tools / Equipment</li>
        <li>Problem Solving and Decision Making</li>
        <li>Route Knowledge</li>
        <li>Self-Management</li>
        <li>Situation Awareness</li>
        <li>System Knowledge</li>
        <li>Teamwork and Leadership</li>
        <li>Train Handling</li>
        <li>Workload Management</li>
      </ul>
    </div>
    <div class="brand" style="left:162px;top:318px;">RAILMETRIC</div>
    <div class="footer-rule"></div>
    <div class="footer"><span>+61 (0)400 555 018</span><span>www.railmetric.com.au</span><span>hello@railmetric.com.au</span></div>
  </section>

  <!-- Page 2 -->
  <section class="page page--2">
    <div class="corner-pattern" role="img" aria-label="Soft decorative brand pattern"></div>
    <div class="tab"></div>
    <div class="copy abs" style="left:22px;top:57px;width:126px;">
      <p>In contrast to other performance marker systems, the current project aims to include both ‘technical’ and ‘non-technical’ skills in an integrated framework, with substantial input from drivers across the industry, both in passenger and freight operations. The aim is to develop a framework that uses a language that describes performance in a way that is relatable to drivers, trainers, and assessors.</p>
    </div>
    <div class="rule" style="left:22px;top:121px;width:118px;"></div>
    <div class="copy abs" style="left:22px;top:130px;width:118px;">
      <p class="callout-title">Underlying competencies:</p>
      <p class="callout-body" style="margin-top:0">The underpinning knowledge and skills required by a train driver, to perform a range of different tasks effectively. Underlying competencies include both ‘technical’ and ‘non-technical’ skills. They are not specific to one driving task, but help build resilient performance across all tasks, conditions or situations that a driver may encounter.</p>
    </div>
    <div class="rule" style="left:22px;top:185px;width:118px;"></div>
    <div class="photo" style="left:21px;top:192px;width:224px;height:144px;background:linear-gradient(160deg,#2b2f6a 0%,#6a5ab0 35%,#9a86c8 50%,#1c1f33 75%,#0d0f18 100%);" role="img" aria-label="Photo of a driver's cab view looking along the track at dusk"></div>
    <div class="footer-rule"></div>
    <div class="footer"><span>+61 (0)400 555 018</span><span>www.railmetric.com.au</span><span>hello@railmetric.com.au</span></div>
  </section>

  <!-- Page 3 -->
  <section class="page page--3">
    <div class="corner-pattern" role="img" aria-label="Soft decorative brand pattern"></div>
    <div class="tab"></div>
    <h2 class="heading" style="left:21px;top:84px;width:230px;">
      <span class="light">What are the benefits for</span><br>
      <span class="bold">Participating organisations?</span>
    </h2>
    <div class="copy abs" style="left:21px;top:117px;width:142px;">
      <p>All participating rail organisations will receive a copy of the performance indicator framework, which they are free to use or adapt for application within their own operation. A summary report will also be provided, outlining the methodology and aggregated results of the data collection activities. All results will be presented in a de-identified way, to ensure the anonymity of participating organisations and individuals.</p>
    </div>
    <h2 class="heading" style="left:21px;top:176px;width:150px;">
      <span class="light">What is</span> <span class="bold">involved?</span>
    </h2>
    <div class="copy abs" style="left:21px;top:196px;width:143px;height:142px;overflow:hidden;">
      <p>Participating organisations will be invited to provide in-kind support for the following activities during the period April – June 2020:</p>
      <ul class="bullets" style="margin-top:0">
        <li><span class="item-label">Interviews with volunteer Driver participants:</span> individual discussions with our researchers about drivers’ previous experiences, to gather information about expert driving strategies and positive techniques used in normal and abnormal operations.</li>
        <li><span class="item-label">Initial workshop:</span> a facilitated group workshop to understand the links between underlying competencies and driving tasks, and to understand Drivers’ perceptions of what each underlying competency looks like in practice.</li>
        <li><span class="item-label">Driver Training Survey:</span> a voluntary survey will be distributed, requesting Driver Trainers’ and Assessors’ views on the importance of underlying competencies in driving performance, and further data about expert strategies and techniques.</li>
        <li><span class="item-label">Follow-up workshop:</span> a facilitated group workshop to test and refine the performance indicators. Where possible, indicators will be tested through participants providing ratings of a video sample of actual performance.</li>
      </ul>
    </div>
    <div class="photo" style="left:172px;top:128px;width:74px;height:208px;background:linear-gradient(180deg,#5a7fa8 0%,#8aa6c0 25%,#4a4a52 55%,#9a9aa0 80%,#3a3a40 100%);" role="img" aria-label="Photo of city railway tracks leading between tall buildings"></div>
    <div class="footer-rule"></div>
    <div class="footer"><span>+61 (0)400 555 018</span><span>www.railmetric.com.au</span><span>hello@railmetric.com.au</span></div>
  </section>

  <!-- Page 4 -->
  <section class="page page--4">
    <div class="corner-pattern" role="img" aria-label="Soft decorative brand pattern"></div>
    <div class="tab"></div>
    <h2 class="heading" style="left:22px;top:85px;width:150px;">
      <span class="light">Support from</span><br>
      <span class="bold">Participating<br>organisations</span>
    </h2>
    <div class="copy abs" style="left:22px;top:127px;width:90px;">
      <p>It is anticipated that workshops will be run in Brisbane, Sydney and Melbourne. We would appreciate support from participating organisations in providing a workshop venue where possible. Apart from the in-kind support of providing access to personnel and a meeting room, there is no cost associated with participation in the project.</p>
      <p>In addition to the activities involving industry participation, we will also be completing a detailed task analysis and analysing incident reports and other publicly available data, to help inform the development of the framework.</p>
    </div>
    <div class="quote-bar"></div>
    <p class="quote">We look forward to hearing from organisations interested in being part of this landmark project.</p>
    <div class="brand" style="left:163px;top:310px;">RAILMETRIC</div>
    <div class="footer-rule"></div>
    <div class="footer"><span>+61 (0)400 555 018</span><span>www.railmetric.com.au</span><span>hello@railmetric.com.au</span></div>
  </section>
</body>
</html>
```